Gloss Line auto detail

Looking for a flyer for my auto detail business
Hand Wash
• Clay Bar Application
• Machine Buff Wax / Compound /
Polish Paint Correction
• Clean Interior & Exterior Glass
• Vacuum, Shampoo, & Steam Clean
Upholstery, Carpets, Seats, Mats, & Trunk
• Pet Hair Removal
• Clean headliner
• Clean Doors/ Trunk/Hood Jambs
• Air Blow & Clean all Cracks & Crevices • Clean & Shine Protect All Vinyl/
Dash/Door Panels/Middle Console
Cleaning/Conditioning of Leather
• Clean, Treat, Dress, & Polish Tires,
Rims, & Wheel Wells
• Bug & Tar Removal
• Dress Black Exterior Plastic
• Minor Scratch Removal
• Engine Compartment Detail
Headlight Restoration (if needed)
• Interior Fragrance
• DRY ICE BLASTING
At Gloss Line Auto Detail, we pride ourselves on providing a unique and exceptional experience that sets us apart from other detailers. Here are a few key factors that make us stand out:
1. Attention to Detail: We live up to our name by going above and beyond in every aspect of our car detailing services. Our team of skilled technicians pays meticulous attention to every nook and cranny of your vehicle, ensuring that it receives the highest level of care and precision.
2. Customized Solutions: We understand that each car is unique, and so are our clients' needs. That's why we offer personalized solutions tailored to your specific requirements. Whether you need a basic wash and wax or a comprehensive paint correction, we will work with you to create a customized detailing plan that meets your expectations.
3. Cutting-Edge Technology: We stay at the forefront of the industry by utilizing the latest tools, products, and techniques. Our team is trained in the most advanced detailing methods, allowing us to achieve superior results and deliver a finish that exceeds your expectations.
4. Exceptional Customer Service: We believe in providing not only exceptional car detailing but also an exceptional customer experience. Our friendly and knowledgeable staff is always ready to assist you, answer your questions, and ensure that you have a positive and enjoyable experience at our facility.
5. Eco-Friendly Practices: We are committed to reducing our environmental impact by using eco-friendly cleaning products and techniques. Our detailing processes are designed to minimize water usage and waste generation, making us a responsible choice for those who care about the planet.
These factors, combined with our passion for cars and dedication to excellence, make Gloss Line Auto Detail the premier choice for discerning car owners who seek a truly exceptional detailing experience.
We offer mobile services as well
Address 742 Fernhollow Ave. N., Renton, WA 98061

```html
<!DOCTYPE html>
<html lang="en">
<head>
<meta charset="utf-8">
<title>Gloss Line Auto Detail — Flyer</title>
<link rel="stylesheet" href="https://fonts.googleapis.com/css2?family=Exo+2:ital,wght@0,700;1,800;1,900&family=Barlow+Condensed:ital,wght@1,600;1,700&family=Poppins:wght@400;500;600;700&display=swap">
<style>
  :root {
    --stage: #c8c8c8;
    --flyer-dark: #111111;
    --flyer-mid: #1e1e1e;
    --red: #e0161b;
    --red-panel: #9c1312;
    --red-panel-dark: #6e0c0b;
    --white: #ffffff;
    --silver-light: #f4f4f4;
    --silver-dark: #8a8a8a;
    --number-grey: #3c3c3c;
    --rule: #3a3a3a;
  }
  * { box-sizing: border-box; margin: 0; padding: 0; }
  html, body { width: 1200px; height: 908px; overflow: hidden; }
  body { background: var(--stage); font-family: "Poppins", sans-serif; color: var(--white); }

  .flyer {
    position: absolute; left: 249px; top: 0; width: 702px; height: 908px; overflow: hidden;
    background: radial-gradient(ellipse at 50% 30%, var(--flyer-mid) 0%, var(--flyer-dark) 70%);
  }
  .abs { position: absolute; }

  .kicker {
    left: 0; width: 702px; top: 48px; text-align: center;
    font-family: "Exo 2", sans-serif; font-style: italic; font-weight: 800;
    font-size: 19px; letter-spacing: 9px;
  }
  .kicker-rule { top: 60px; height: 1px; width: 178px; background: #5a5a5a; }
  .headline-red {
    left: 0; width: 702px; top: 70px; text-align: center;
    font-family: "Exo 2", sans-serif; font-style: italic; font-weight: 900;
    font-size: 36px; color: var(--red); letter-spacing: 1px; line-height: 40px;
  }
  .headline-silver {
    left: 0; width: 702px; top: 100px; text-align: center;
    font-family: "Exo 2", sans-serif; font-style: italic; font-weight: 900;
    font-size: 68px; line-height: 76px; letter-spacing: 2px;
    background: linear-gradient(180deg, var(--silver-light) 0%, var(--silver-light) 45%, var(--silver-dark) 55%, #d8d8d8 100%);
    -webkit-background-clip: text; background-clip: text; color: transparent;
  }
  .headline-bar { left: 332px; top: 170px; width: 38px; height: 3px; background: var(--red); }
  .intro {
    left: 40px; width: 622px; top: 189px; text-align: center;
    font-size: 11.3px; font-weight: 600; line-height: 13.5px;
  }

  .service-panel {
    left: 0; top: 260px; width: 249px; height: 457px;
    background: linear-gradient(135deg, var(--red-panel) 0%, #b51716 50%, var(--red-panel-dark) 100%);
    clip-path: polygon(0 0, 190px 0, 249px 44px, 249px 100%, 0 100%);
  }
  .service-group { position: absolute; left: 46px; width: 200px; }
  .service-title { font-size: 14.5px; font-weight: 700; line-height: 16px; }
  .service-note { font-size: 8px; font-weight: 600; }
  .service-list { list-style: none; margin-top: 3px; }
  .service-list li {
    position: relative; padding-left: 12px;
    font-size: 9.3px; line-height: 11px; margin-bottom: 1.6px;
  }
  .service-list li::before {
    content: "✓"; position: absolute; left: 0; top: 2px;
    width: 7px; height: 7px; border-radius: 50%;
    background: var(--white); color: var(--red-panel);
    font-size: 6px; line-height: 7px; text-align: center; font-weight: 700;
  }
  .service-rule { position: absolute; left: 46px; width: 177px; height: 1px; background: rgba(0,0,0,0.35); }

  .factor { position: absolute; width: 140px; }
  .factor-number {
    position: absolute; left: -56px; top: -6px; width: 50px; text-align: right;
    font-family: "Exo 2", sans-serif; font-style: italic; font-weight: 900;
    font-size: 62px; line-height: 62px; color: var(--number-grey);
  }
  .factor-title {
    font-family: "Barlow Condensed", sans-serif; font-style: italic; font-weight: 700;
    color: var(--red); font-size: 13.5px; line-height: 12.5px; text-transform: uppercase; letter-spacing: 0.3px;
  }
  .factor-body { margin-top: 5px; font-size: 8.1px; line-height: 9.65px; color: #e8e8e8; }

  .rule-h { height: 1px; background: linear-gradient(90deg, transparent, var(--rule), transparent); }
  .rule-v { width: 1px; background: linear-gradient(180deg, transparent, var(--rule) 20%, var(--rule) 80%, transparent); }

  .car-photo {
    left: 432px; top: 585px; width: 270px; height: 275px;
    background: radial-gradient(ellipse at 60% 50%, #b0141a 0%, #5a0a0d 45%, transparent 75%);
  }

  .brand-mark { left: 68px; top: 749px; width: 108px; height: 108px; border-radius: 50%; background: var(--red); }
  .brand-name {
    left: 30px; top: 790px; width: 184px; text-align: center;
    font-size: 20px; font-weight: 700; line-height: 24px; color: var(--white);
  }

  .offer-title {
    left: 336px; top: 592px;
  }
  .offer-heading {
    left: 336px; top: 595px;
  }
  .offer {
    left: 333px; top: 842px;
  }
  .we-offer {
    left: 336px; top: 842px;
  }
  .cta-red {
    left: 337px; top: 841px;
  }
  .cta-big {
    left: 337px; top: 753px;
    font-family: "Barlow Condensed", sans-serif; font-style: italic; font-weight: 700;
    font-size: 34px; line-height: 34px; color: var(--red); text-transform: uppercase;
  }
  .cta-sub {
    left: 334px; top: 784px;
    font-family: "Barlow Condensed", sans-serif; font-style: italic; font-weight: 700;
    font-size: 19px; line-height: 20px; text-transform: uppercase;
  }
  .address-pin { left: 332px; top: 825px; }
  .address {
    left: 357px; top: 817px; font-size: 13.5px; line-height: 17px; font-weight: 500;
  }
</style>
</head>
<body>
<main class="flyer">
  <div class="abs kicker-rule" style="left:62px"></div>
  <div class="abs kicker-rule" style="left:462px"></div>
  <p class="abs kicker">EXPERIENCE</p>
  <h1 class="abs headline-red">UNIQUE &amp; EXCEPTIONAL</h1>
  <h2 class="abs headline-silver">AUTO DETAIL</h2>
  <div class="abs headline-bar"></div>
  <p class="abs intro">At Gloss Line Auto Detail, we pride ourselves on providing a unique and exceptional experience that sets us apart from other detailers. Here are a few key factors that make us stand out</p>

  <section class="abs service-panel">
    <div class="service-group" style="top:18px">
      <h3 class="service-title">Hand Wash</h3>
      <ul class="service-list">
        <li>Clay Bar Application</li>
        <li>Machine Buff Wax / Compound /</li>
      </ul>
    </div>
    <div class="service-rule" style="top:78px"></div>
    <div class="service-group" style="top:90px">
      <h3 class="service-title">Polish Paint Correction</h3>
      <ul class="service-list">
        <li>Clean Interior &amp; Exterior Glass</li>
        <li>Vacuum, Shampoo, &amp; Steam Clean</li>
      </ul>
    </div>
    <div class="service-rule" style="top:149px"></div>
    <div class="service-group" style="top:162px; width:205px">
      <h3 class="service-title">Upholstery, Carpets,<br>Seats, Mats, &amp; Trunk</h3>
      <ul class="service-list">
        <li>Pet Hair Removal</li>
        <li>Clean headliner</li>
        <li>Clean Doors/ Trunk/Hood Jambs</li>
        <li>Air Blow &amp; Clean all Cracks &amp; Crevices</li>
        <li>Clean &amp; Shine Protect All Vinyl/Dash/ Door Panels/Middle Console Cleaning/Conditioning of Leather</li>
        <li>Clean, Treat, Dress, &amp; Polish Tires, Rims, &amp; Wheel Wells</li>
        <li>Bug &amp; Tar Removal</li>
        <li>Dress Black Exterior Plastic</li>
        <li>Minor Scratch Removal</li>
        <li>Engine Compartment Detail</li>
      </ul>
    </div>
    <div class="service-rule" style="top:372px"></div>
    <div class="service-group" style="top:384px; left:45px">
      <h3 class="service-title">Headlight Restoration</h3>
      <p class="service-note">(if needed)</p>
      <ul class="service-list" style="margin-top:1px">
        <li>Interior Fragrance</li>
        <li>DRY ICE BLASTING</li>
      </ul>
    </div>
  </section>

  <div class="abs rule-v" style="left:584px; top:255px; height:385px"></div>
  <div class="abs rule-h" style="left:300px; top:402px; width:180px"></div>
  <div class="abs rule-h" style="left:510px; top:402px; width:180px"></div>
  <div class="abs rule-h" style="left:300px; top:570px; width:180px"></div>

  <article class="factor" style="left:317px; top:260px">
    <span class="factor-number">1</span>
    <h4 class="factor-title">Attention to Detail</h4>
    <p class="factor-body">We live up to our name by going above and beyond in every aspect of our car detailing services. Our team of skilled technicians pays meticulous attention to every nook and cranny of your vehicle, ensuring that it receives the highest level of care and precision.</p>
  </article>
  <article class="factor" style="left:317px; top:429px">
    <span class="factor-number">2</span>
    <h4 class="factor-title">Customized Solutions</h4>
    <p class="factor-body">We understand that each car is unique, and so are our clients' needs. That's why we offer personalized solutions tailored to your specific requirements. Whether you need a basic wash and wax or a comprehensive paint correction, we will work with you to create a customized detailing plan that meets your expectations.</p>
  </article>
  <article class="factor" style="left:317px; top:596px; width:145px">
    <span class="factor-number">3</span>
    <h4 class="factor-title">Cutting Edge Technology</h4>
    <p class="factor-body">We stay at the forefront of the industry by utilizing the latest tools, products, and techniques. Our team is trained in the most advanced detailing methods, allowing us to achieve superior results and deliver a finish that exceeds your expectations.</p>
  </article>
  <article class="factor" style="left:532px; top:260px; width:135px">
    <span class="factor-number">4</span>
    <h4 class="factor-title">Exceptional Customer Service</h4>
    <p class="factor-body">We believe in providing not only exceptional car detailing but also an exceptional customer experience. Our friendly and knowledgeable staff is always ready to assist you, answer your questions, and ensure that you have a positive and enjoyable experience at our facility.</p>
  </article>
  <article class="factor" style="left:531px; top:429px; width:130px">
    <span class="factor-number">5</span>
    <h4 class="factor-title">Eco-Friendly Practices</h4>
    <p class="factor-body">We live up to our name by going above and beyond in every aspect of our car detailing services. Our team of skilled technicians pays meticulous attention to every nook and cranny of your vehicle, ensuring that it receives the highest level of care and precision.</p>
  </article>

  <div class="abs car-photo" role="img" aria-label="Photo of a glossy red sports car with bright headlights, front three-quarter view"></div>

  <div class="abs brand-mark"></div>
  <p class="abs brand-name">Gloss Line</p>

  <p class="abs cta-big">We Offer</p>
  <p class="abs cta-sub">Mobile Services as well</p>
  <svg class="abs address-pin" width="18" height="26" viewBox="0 0 18 26" aria-hidden="true">
    <path d="M9 0C4 0 0 4 0 9c0 6.5 9 17 9 17s9-10.5 9-17C18 4 14 0 9 0z" fill="#e0161b"/>
    <circle cx="9" cy="9" r="3.5" fill="#111111"/>
  </svg>
  <p class="abs address">Address 742 Fernhollow Ave.<br>N., Renton, WA 98061</p>
</main>
</body>
</html>
```